KEP Business Card

the business card should be double sided.
Will need to be Korean on one side and english on the other.
it will need to have:

address
website
skype
phone
cell
fax
name
title
email

just put in dummy details to start - i will then give you correct info once we have the format right.

Also - if you feel creative about the logo we are happy to make some amendments to it so it looks right. We are still at early stages with the logo so happy if you have suggestions around the logo concept.
Updates

The deadline for this has been brought forward to Wednesday 11th December. We can not review any designs after this date.

we will need to make a decision by Wednesday 11th December, so please have designs in by this date and not by the deadline set by lumahive

Target Market(s)

large companies, executives

Industry/Entity Type

Business

Colors

Designer to choose colors to be used in the design.

Requirements
Must have
• double sided - english on one side and korean on the other. we will give you korean wording once we have a design we like.

```html
<!DOCTYPE html>
<html lang="en">
<head>
<meta charset="utf-8">
<title>KEP Business Card</title>
<link rel="stylesheet" href="https://fonts.googleapis.com/css2?family=Jost:wght@400;600&display=swap">
<style>
  :root {
    --page-bg: #ffffff;
    --card-dark: #2f2f2f;
    --card-mid: #4a4a4a;
    --card-glow: #8d8d8f;
    --ink-light: #f2f2f2;
    --ink-dark: #141414;
    --groove-dark: #1c1c1c;
    --groove-light: rgba(255,255,255,0.18);
  }
  * { margin: 0; padding: 0; box-sizing: border-box; }
  html, body {
    width: 1200px;
    height: 900px;
    overflow: hidden;
    background: var(--page-bg);
    font-family: "Jost", "Futura", sans-serif;
  }
  .canvas {
    position: relative;
    width: 1200px;
    height: 900px;
  }
  .business-card {
    position: absolute;
    left: 290px;
    width: 620px;
    height: 354px;
    background:
      radial-gradient(ellipse 290px 230px at 52% 42%, var(--card-glow) 0%, var(--card-mid) 45%, var(--card-dark) 100%);
    box-shadow: 0 6px 18px rgba(0,0,0,0.35);
  }
  .card-front { top: 58px; }
  .card-back { top: 488px; }
  .divider {
    position: absolute;
    left: 292px;
    top: 78px;
    width: 3px;
    height: 204px;
    background: linear-gradient(to right, var(--groove-dark), var(--groove-light));
    border-radius: 2px;
  }
  .brand {
    position: absolute;
    left: 50px;
    top: 140px;
    width: 210px;
    text-align: center;
    color: var(--ink-dark);
  }
  .brand-mark {
    width: 30px;
    height: 30px;
    margin: 0 auto 9px;
    background: var(--ink-dark);
  }
  .brand-name {
    font-size: 30px;
    font-weight: 600;
    letter-spacing: 2px;
    line-height: 1;
  }
  .brand-website {
    margin-top: 18px;
    font-size: 18px;
    font-weight: 400;
    letter-spacing: 1px;
  }
  .identity {
    position: absolute;
    left: 340px;
    top: 52px;
    color: var(--ink-light);
    text-shadow: 0 1px 2px rgba(0,0,0,0.5);
  }
  .person-name {
    font-size: 30px;
    font-weight: 400;
    text-transform: uppercase;
    line-height: 1;
    letter-spacing: 0.5px;
  }
  .person-title {
    font-size: 23px;
    font-weight: 400;
    line-height: 1;
    margin-top: 3px;
    margin-left: 6px;
  }
  .contact-list {
    position: absolute;
    left: 340px;
    top: 160px;
    list-style: none;
    color: var(--ink-light);
    font-size: 17px;
    line-height: 20px;
    text-shadow: 0 1px 2px rgba(0,0,0,0.5);
  }
</style>
</head>
<body>
<main class="canvas">
  <section class="business-card card-front" aria-label="KEP business card, front">
    <div class="brand">
      <div class="brand-mark"></div>
      <div class="brand-name">KEP</div>
      <div class="brand-website">www.website.com</div>
    </div>
    <div class="divider"></div>
    <div class="identity">
      <h1 class="person-name">Owen Laird</h1>
      <p class="person-title">director</p>
    </div>
    <ul class="contact-list">
      <li>phone: 0000000</li>
      <li>cell: 0000000</li>
      <li>fax: 0000000</li>
      <li>email: ol@kep.com</li>
      <li>skype: kep__</li>
      <li>address: harborlane 12</li>
    </ul>
  </section>

  <section class="business-card card-back" aria-label="KEP business card, reverse">
    <div class="brand">
      <div class="brand-mark"></div>
      <div class="brand-name">KEP</div>
      <div class="brand-website">www.website.com</div>
    </div>
    <div class="divider"></div>
    <div class="identity">
      <h2 class="person-name">Owen Laird</h2>
      <p class="person-title">director</p>
    </div>
    <ul class="contact-list">
      <li>phone: 0000000</li>
      <li>cell: 0000000</li>
      <li>fax: 0000000</li>
      <li>email: ol@kep.com</li>
      <li>skype: kep__</li>
      <li>address: harborlane 12</li>
    </ul>
  </section>
</main>
</body>
</html>
```